International Student Travel Company needs a web page re-designed

Halvard Tours is a worldwide leader in student educational and performing arts travel programs. We provide high-quality tours that exceed the expectations of our participants/customers and enhance a student's learning experiences. Our mission is to forever change how every student sees the world around them. Our company has 3 distinct brands: Halvard Tours (www.halvardtours.example), Meridale Tours (www.meridaletours.example) and Pellwood Legacy Tours & Music Galas (www.pellgala.example).

As part of our travel programs, we offer participants the option to purchase travel insurance. We are looking to re-design the page that offers each participant the option to buy insurance during their online registration process to maximize the number of customers who purchase the recommended option. The registration process is set up behind a password protected registration website.

Here is a link to view the current page for each brand:
https://accounts.halvardtours.example/tech/demo/8656
https://accounts.meridaletours.example/tech/demo/8656
https://accounts.pellgala.example/tech/demo/8656

We are attaching the HTML for the current page so you can start with the current format that this design is a part of- for example, the header & footer and the "Registration Step # section".

Please note that this current design was created for the "Meridale Tours" brand as you may note the use of the orange color on the page. We would like to design the page so that we can easily implement the same design for all 3 brands. As you will see from looking at the brands online, they all share a similar blue that can be used where we need a color as you will see on our SAMPLE mock-up that we have included as an attachment.

In our SAMPLE mock-up (file attached named "SAMPLE webpage mock-up.pdf") we have icons at the top of the insurance option which is meant to be a link to a PDF that is an advertisement for each type of travel insurance. So, however you decide to design that element, please make sure to include that as a link that will open a PDF in a new tab. The "None" option will open up the PDF attached named "Note to Parents.pdf". The "Scholar Prime" option will open up the PDF attached named "Odette & Marla.pdf". The "Scholar Prime with CFAR" option will open up the PDF attached named "CFAR.pdf".

The sample mock-up is just a sample draft idea of how we would want it to look. Please feel free to re-design completely or as close to this design as you wish using your best design judgment. The goal is to make it look very professional and convince customers to select the recommended "Scholar Prime with CFAR" option as this will fully protect them in case they need to cancel.

It is very important to use all the copy as its presented since the language has all been approved by the insurance company's compliance team.

*VERY IMPORTANT*
Please design this so that it is MOBILE friendly. Many of our customers register for our trips on their mobile devices. So, because we are presenting 3 options to compare we need to make sure the design works well on small mobile screens. So, please present your designs for both large computer screens and small mobile devices so we can see how it would look at the various different screen sizes.

Please let us know if you have any questions or require any more info from us to get started. We are looking forward to seeing your designs!

-Halvard Tours Marketing Team

```html
<!DOCTYPE html>
<html lang="en">
<head>
<meta charset="utf-8">
<title>Halvard Tours – Registration Step 5/8 – Travel Protection</title>
<link href="https://fonts.googleapis.com/css2?family=Roboto:wght@400;500;700&display=swap" rel="stylesheet">
<style>
:root{
  --brand-blue:#0b3f9e;
  --link-blue:#1556c9;
  --heading-blue:#1747a6;
  --alert-red:#d3303a;
  --notice-yellow:#ffb900;
  --footer-blue:#0a68ad;
  --panel-bg:#f2f4f9;
  --rule:#e3e6ec;
  --ink:#222;
  --muted:#555;
  --badge-green:#6db33f;
}
*{box-sizing:border-box;margin:0;padding:0}
html,body{width:800px;height:1200px;overflow:hidden;background:#fff}
body{font-family:"Roboto",Arial,sans-serif;color:var(--ink)}
.board{position:absolute;left:0;top:0;width:1568px;height:2352px;transform:scale(.5102);transform-origin:0 0}
.abs{position:absolute}
.board-title{position:absolute;font-weight:700;font-size:34px;color:#000}
.icon{display:inline-block;vertical-align:top}

/* ---------- desktop ---------- */
.notice-bar{left:0;top:130px;width:1003px;height:35px;background:var(--notice-yellow);font-size:10px;font-weight:500;text-align:center;line-height:35px}
.site-header{left:0;top:165px;width:1003px;height:52px;border-bottom:1px solid var(--rule)}
.brand{display:flex;align-items:center;gap:8px}
.brand-mark{border-radius:50%;background:var(--alert-red)}
.brand-name{color:var(--alert-red);font-weight:400}
.session{font-size:9px;color:var(--muted)}
.session a{color:var(--alert-red);text-decoration:none}
.hero-photo{background:linear-gradient(180deg,#6e9fd6 0%,#a9c7e8 40%,#8fae7a 75%,#5d7f4c 100%)}
.hero-band{background:var(--brand-blue);color:#fff;display:flex;align-items:center}
.partner-badge{background:#fff;border-radius:3px}
.hero-band p{font-weight:500}
.reg-title{display:flex;justify-content:space-between;align-items:baseline;color:#333}
.reg-title .step b{color:var(--alert-red);font-weight:500}
.tour-box{border:1px solid var(--rule);background:#fff}
.tour-box .box-head{background:#f7f7f9;border-bottom:1px solid var(--rule);color:#333}
.tour-box p{color:var(--muted)}
.tour-box p b{color:#333;font-weight:500}
.offer-panel{background:var(--panel-bg)}
.offer-heading{color:var(--heading-blue);font-weight:700}
.copy{color:#222}
.prompt{color:var(--alert-red);font-weight:500}
.plans-band{background:var(--brand-blue)}
.plan{position:absolute;background:#fff;border-top:3px solid var(--link-blue);text-align:center}
.plan-flag{position:absolute;background:var(--alert-red);color:#fff;text-align:center}
.plan-name{color:var(--heading-blue);font-weight:500;text-transform:uppercase}
.plan-price{color:var(--heading-blue);font-weight:500}
.plan-price sup{font-size:.5em}
.plan-lead{font-weight:700;color:#222}
.plan-list{list-style:none;text-align:left}
.plan-list li{display:flex;gap:4px;color:#444}
.plan-list li.no{color:var(--alert-red)}
.plan-list li.dot::before{content:"";flex:none;width:4px;height:4px;border-radius:50%;background:var(--link-blue);margin-top:3px}
.more-link{position:absolute;left:0;right:0;color:var(--heading-blue);font-weight:700;display:flex;justify-content:center;align-items:center;gap:6px;text-decoration:none}
.select-btn{position:absolute;background:var(--link-blue);color:#fff;font-weight:700;border-radius:16px;text-align:center}
.benefits{border-collapse:collapse}
.benefits th{text-align:left;font-weight:500;vertical-align:middle}
.benefits td{border-top:1px solid var(--rule);vertical-align:middle;color:#333}
.benefits td.name{font-weight:500;color:#222}
.benefits thead{background:#f7f8fb}
.notes p{color:#444}
.limits-btn{background:var(--link-blue);color:#fff;border-radius:12px;text-align:center}
.site-footer{background:var(--footer-blue);color:#fff;font-weight:700}
.secure-badge{background:#fff;border:1px solid #bbb;border-radius:2px}
.secure-badge i{position:absolute;left:3px;top:3px;bottom:3px;width:14px;background:var(--badge-green);border-radius:2px}
.side-tab{left:0;top:372px;width:15px;height:118px;background:#fff;border:2px solid var(--link-blue);border-left:0;border-radius:0 4px 4px 0}
.side-tab span{position:absolute;left:1px;top:110px;transform:rotate(-90deg);transform-origin:0 0;white-space:nowrap;font-size:8px;color:var(--link-blue);font-weight:500;width:110px}
.hamburger{background:var(--link-blue)}
.hamburger i{position:absolute;left:5px;right:5px;height:2px;background:#fff}
</style>
</head>
<body>
<svg width="0" height="0" style="position:absolute">
  <symbol id="tick" viewBox="0 0 10 10"><path d="M1 5.5l2.5 2.5L9 2" fill="none" stroke="#1556c9" stroke-width="1.4"/></symbol>
  <symbol id="cross" viewBox="0 0 10 10"><path d="M1.5 1.5l7 7M8.5 1.5l-7 7" fill="none" stroke="#d3303a" stroke-width="1.2"/></symbol>
  <symbol id="arrow" viewBox="0 0 16 10"><path d="M0 5h14M10 1l4 4-4 4" fill="none" stroke="#1747a6" stroke-width="1.6"/></symbol>
</svg>

<main class="board">

<!-- ================= DESKTOP ================= -->
<h1 class="board-title" style="left:185px;top:50px">Desktop view</h1>

<div class="abs notice-bar">For Coronavirus (COVID-19) Updates Please Click Here</div>
<header class="abs site-header">
  <div class="abs brand" style="left:188px;top:8px">
    <span class="brand-mark" style="width:36px;height:36px"></span>
    <span class="brand-name" style="font-size:20px">Halvard Tours</span>
  </div>
  <div class="abs session" style="left:633px;top:19px">signed on as webuser@mail.example &nbsp;&nbsp; <a href="#">[Logout]</a></div>
</header>
<div class="abs side-tab"><span>Questions? Comments?</span></div>

<div class="abs hero-photo" role="img" aria-label="Group of smiling students taking a selfie in front of the Eiffel Tower" style="left:184px;top:241px;width:420px;height:280px"></div>
<div class="abs hero-band" style="left:192px;top:463px;width:404px;height:58px">
  <div style="width:114px;height:58px;display:flex;align-items:center;justify-content:center"><span class="partner-badge" style="width:80px;height:22px"></span></div>
  <p style="font-size:9.5px;line-height:12px;padding-right:6px">Travel Insurance is optional, but unexpected events are always a possibility… and without the Scholar Prime Group Travel Protection, you might lose up to 100% of your trip investment.</p>
</div>

<div class="abs reg-title" style="left:618px;top:238px;width:199px">
  <span style="font-size:18px">Registration</span><span class="step" style="font-size:18px;font-weight:500">Step <b>5</b>/8</span>
</div>
<section class="abs tour-box" style="left:618px;top:264px;width:199px;height:106px">
  <div class="box-head" style="font-size:8px;padding:6px 8px">YOUR TOUR INFORMATION</div>
  <div style="padding:8px 8px;font-size:7.5px;line-height:16.5px">
    <p>Group Name: <b>Lakemont Elementary School</b></p>
    <p>Tour Name: <b>Two Days Test Tour</b></p>
    <p>Tour Dates: <b>3/2/2021</b></p>
    <p>Tour Organizer: <b>Mr. Dalton Reyes</b></p>
  </div>
</section>

<section class="abs offer-panel" style="left:184px;top:521px;width:420px;height:529px">
  <h2 class="abs offer-heading" style="left:8px;top:19px;font-size:16px">Protect your Trip Investment!</h2>
  <div class="abs copy" style="left:8px;top:50px;width:400px;font-size:8.5px;line-height:13px">
    <p>Wayfarer Assure Group, a leading provider of group travel insurance, offers participants the opportunity to protect their travel investment.</p>
    <p style="margin-top:13px">This program offers an array of <b>travel protection</b> benefits including 24/7 Worldwide Non-Insurance Assistance Services as well as Trip Cancellation, Trip Interruption, Medical Expense, Baggage and Personal Effects, and more travel insurance coverages such as the Cancel for Any Reason (CFAR) option, if eligible.</p>
  </div>
  <p class="abs prompt" style="left:14px;top:159px;font-size:12px">To start, please enter your total Trip Cost: $_______</p>
</section>

<div class="abs plans-band" style="left:184px;top:965px;width:420px;height:85px"></div>

<article class="plan" style="left:192px;top:729px;width:130px;height:291px">
  <h3 class="plan-name" style="font-size:9px;margin-top:14px">None</h3>
  <p class="plan-price" style="font-size:12px;margin-top:6px"><sup>$</sup>0</p>
  <p class="plan-lead" style="font-size:7.5px;line-height:10px;margin:16px 14px 0">Potentially lose 100% of your tour cost</p>
  <ul class="plan-list" style="font-size:7.5px;margin:16px 8px 0"><li class="dot">No Payment Protection</li></ul>
  <a class="more-link" href="#" style="top:250px;font-size:7.5px">MORE INFORMATION <svg class="icon" width="14" height="9"><use href="#arrow"/></svg></a>
</article>
<div class="select-btn" style="left:215px;top:1010px;width:84px;height:22px;font-size:9px;line-height:22px">SELECT</div>

<article class="plan" style="left:328px;top:729px;width:130px;height:291px">
  <h3 class="plan-name" style="font-size:9px;margin-top:14px">Scholar Prime</h3>
  <p class="plan-price" style="font-size:12px;margin-top:6px"><sup>$</sup>100</p>
  <p class="plan-lead" style="font-size:7.5px;line-height:10px;margin:16px 8px 0">Protects your trip investment for covered reasons only</p>
  <ul class="plan-list" style="font-size:7px;line-height:10.5px;margin:10px 4px 0 5px">
    <li><svg class="icon" width="8" height="8"><use href="#tick"/></svg><span>Trip Cancellation coverage provides a 100% refund if you need to cancel for covered reasons</span></li>
    <li style="margin-top:6px"><svg class="icon" width="8" height="8"><use href="#tick"/></svg><span>Includes additional coverages as per below Schedule</span></li>
    <li class="no" style="margin-top:9px"><svg class="icon" width="8" height="8"><use href="#cross"/></svg><span>Does NOT include Cancel for Any Reason (CFAR)***</span></li>
    <li class="no" style="margin-top:7px"><svg class="icon" width="8" height="8"><use href="#cross"/></svg><span>No coverage for cancellations due to fear of a pandemic</span></li>
  </ul>
  <a class="more-link" href="#" style="top:250px;font-size:7.5px">MORE INFORMATION <svg class="icon" width="14" height="9"><use href="#arrow"/></svg></a>
</article>
<div class="select-btn" style="left:349px;top:1008px;width:84px;height:22px;font-size:9px;line-height:22px">SELECT</div>

<div class="plan-flag" style="left:466px;top:714px;width:130px;height:17px;font-size:8px;line-height:17px">RECOMMENDED</div>
<article class="plan" style="left:466px;top:731px;width:130px;height:289px;border-top:0">
  <h3 class="plan-name" style="font-size:9px;line-height:12px;margin-top:14px">Scholar Prime<br>with CFAR</h3>
  <p class="plan-price" style="font-size:12px;margin-top:5px"><sup>$</sup>100</p>
  <p class="plan-lead" style="font-size:7.5px;line-height:10px;margin:6px 6px 0">Protects your trip investment if you need to cancel for any reason***</p>
  <ul class="plan-list" style="font-size:7px;line-height:10.5px;margin:6px 4px 0 5px">
    <li><svg class="icon" width="8" height="8"><use href="#tick"/></svg><span>Trip Cancellation coverage provides a 100% refund if you need to cancel for covered reasons</span></li>
    <li style="margin-top:6px"><svg class="icon" width="8" height="8"><use href="#tick"/></svg><span>Includes additional coverages as per below Schedule</span></li>
    <li style="margin-top:7px"><svg class="icon" width="8" height="8"><use href="#tick"/></svg><span>Includes Cancel for Any Reason (CFAR)***</span></li>
    <li style="margin-top:5px"><svg class="icon" width="8" height="8"><use href="#tick"/></svg><span>Covers cancellation due to fear of a pandemic ***</span></li>
  </ul>
  <a class="more-link" href="#" style="top:246px;font-size:7.5px">MORE INFORMATION <svg class="icon" width="14" height="9"><use href="#arrow"/></svg></a>
</article>
<div class="select-btn" style="left:487px;top:1006px;width:84px;height:22px;font-size:9px;line-height:22px">SELECT</div>

<table class="abs benefits" style="left:184px;top:1060px;width:420px;font-size:7.5px">
  <colgroup><col style="width:142px"><col style="width:52px"><col style="width:106px"><col></colgroup>
  <thead><tr style="height:35px"><th style="font-size:13px;padding-left:8px;padding-top:12px">Benefit</th><th>NONE</th><th>SCHOLAR PRIME</th><th>SCHOLAR PRIME<br>WITH CFAR</th></tr></thead>
  <tbody>
  <tr style="height:30px"><td class="name">CANCEL FOR ANY REASON (CFAR)***</td><td><svg class="icon" width="10" height="10" style="margin-left:4px"><use href="#cross"/></svg></td><td><svg class="icon" width="10" height="10"><use href="#cross"/></svg></td><td><svg class="icon" width="14" height="14" style="margin-left:4px"><use href="#tick"/></svg></td></tr>
  <tr style="height:26px"><td class="name">Trip Cancellation**</td><td><svg class="icon" width="10" height="10" style="margin-left:4px"><use href="#cross"/></svg></td><td>Trip Cost*</td><td>Trip Cost*</td></tr>
  <tr style="height:26px"><td class="name">Trip Interruption**</td><td><svg class="icon" width="10" height="10" style="margin-left:4px"><use href="#cross"/></svg></td><td>150% Trip Cost</td><td>150% Trip Cost</td></tr>
  <tr style="height:26px"><td class="name">Travel Delay – 6 Hours</td><td><svg class="icon" width="10" height="10" style="margin-left:4px"><use href="#cross"/></svg></td><td>$750 ($150/day)</td><td>$750 ($150/day)</td></tr>
  <tr style="height:34px"><td class="name">Missed Connection –<br>3 Hours</td><td><svg class="icon" width="10" height="10" style="margin-left:4px"><use href="#cross"/></svg></td><td>$500</td><td>$500</td></tr>
  <tr style="height:30px"><td class="name">Baggage/Personal Effects</td><td><svg class="icon" width="10" height="10" style="margin-left:4px"><use href="#cross"/></svg></td><td>$1,500</td><td>$1,500</td></tr>
  <tr style="height:22px"><td class="name">Baggage Delay – 24 Hours</td><td><svg class="icon" width="10" height="10" style="margin-left:4px"><use href="#cross"/></svg></td><td>$300</td><td>$300</td></tr>
  <tr style="height:42px"><td class="name">Emergency Medical Evacuation,<br>Medical Repatriation &amp; Return<br>of Remains</td><td><svg class="icon" width="10" height="10" style="margin-left:4px"><use href="#cross"/></svg></td><td>$100,000</td><td>$100,000</td></tr>
  <tr style="height:34px"><td class="name">Accident &amp; Sickness Medical<br>Expense</td><td><svg class="icon" width="10" height="10" style="margin-left:4px"><use href="#cross"/></svg></td><td>$25,000</td><td>$25,000</td></tr>
  <tr style="height:34px"><td class="name">Non-Medical Emergency<br>Evacuation</td><td><svg class="icon" width="10" height="10" style="margin-left:4px"><use href="#cross"/></svg></td><td>$100,000</td><td>$100,000</td></tr>
  <tr style="height:30px;border-bottom:1px solid var(--rule)"><td class="name">Non-Insurance Worldwide<br>Emergency Assistance Services</td><td><svg class="icon" width="10" height="10" style="margin-left:4px"><use href="#cross"/></svg></td><td>Included</td><td>Included</td></tr>
  </tbody>
</table>

<div class="abs notes" style="left:183px;top:1448px;width:420px;font-size:6.8px;line-height:10.5px">
  <p>Coverages may vary and not all coverage is available in all jurisdictions. Totals listed below each coverage are the maximum benefit amount payable.</p>
  <p style="margin-top:10px">* Up to the lesser of the Trip Cost paid or the limit of Coverage for which benefits are requested and the appropriate plan cost has been paid. Maximum limit of $10,000</p>
  <p style="margin-top:10px">** For $0 Trip Cost, there is no Trip Cancellation and Trip Interruption is limited to $500 return air only</p>
  <p style="margin-top:10px">*** CFAR coverage is the lessor of 75% of the nonrefundable trip cost or up to the maximum of $10,000. CFAR is optional and available for purchase on an individual level. Trip cancellation must be 48 hours or more prior to scheduled departure. CFAR must be purchased at the time of plan purchase and with, or before your final payment. CFAR is available if you paid your Travel Supplier for the full cost for all non-refundable trip costs for your trip prior to your cancellation of your trip. For $0 Trip Cost there is no CFAR. <b>This benefit is not available to residents of New York State.</b></p>
</div>
<a class="abs limits-btn" href="#" style="left:184px;top:1605px;width:201px;height:24px;font-size:9.5px;line-height:24px;text-decoration:none">Click here for limitations and exclusions</a>

<footer class="abs site-footer" style="left:0;top:1695px;width:1003px;height:35px;font-size:8px">
  <p class="abs" style="left:313px;top:12px;word-spacing:2px">© 2020 HALVARD TOURS, INC. &nbsp; CONTACT US &nbsp; (800) 555-0142 &nbsp; PRIVACY POLICY &nbsp; RESPONSIBILITY</p>
  <span class="abs secure-badge" style="left:757px;top:10px;width:72px;height:18px"><i></i></span>
</footer>

<!-- ================= MOBILE ================= -->
<h1 class="board-title" style="left:1184px;top:64px">Mobile Responsive</h1>

<header class="abs" style="left:1186px;top:150px;width:196px;height:46px;border-bottom:1px solid var(--rule)">
  <div class="abs brand" style="left:6px;top:7px;gap:5px">
    <span class="brand-mark" style="width:28px;height:28px"></span>
    <span class="brand-name" style="font-size:13px">Halvard Tours</span>
  </div>
  <span class="abs hamburger" style="left:164px;top:10px;width:23px;height:22px"><i style="top:6px"></i><i style="top:10px"></i><i style="top:14px"></i></span>
</header>

<div class="abs reg-title" style="left:1192px;top:213px;width:184px">
  <span style="font-size:13px">Registration</span><span class="step" style="font-size:13px;font-weight:500">Step <b>5</b>/8</span>
</div>
<section class="abs tour-box" style="left:1192px;top:232px;width:183px;height:84px">
  <div class="box-head" style="font-size:5.5px;padding:5px 7px">YOUR TOUR INFORMATION</div>
  <div style="padding:6px 7px;font-size:5.2px;line-height:13px">
    <p>Group Name: <b>Lakemont Elementary School</b></p>
    <p>Tour Name: <b>Two Days Test Tour</b></p>
    <p>Tour Dates: <b>3/2/2021</b></p>
    <p>Tour Organizer: <b>Mr. Dalton Reyes</b></p>
  </div>
</section>

<div class="abs hero-photo" role="img" aria-label="Group of smiling students taking a selfie in front of the Eiffel Tower" style="left:1186px;top:323px;width:196px;height:159px"></div>
<div class="abs hero-band" style="left:1186px;top:425px;width:196px;height:57px">
  <div style="width:54px;display:flex;justify-content:center"><span class="partner-badge" style="width:40px;height:10px"></span></div>
  <p style="font-size:5.8px;line-height:9.3px;font-weight:400;padding-right:4px">Travel Insurance is optional, but unexpected events are always a possibility… and without the Scholar Prime Group Travel Protection, you might lose up to 100% of your trip investment.</p>
</div>

<section class="abs offer-panel" style="left:1186px;top:482px;width:196px;height:1040px">
  <h2 class="abs offer-heading" style="left:9px;top:13px;font-size:12.5px;line-height:16px">Protect your Trip<br>Investment!</h2>
  <div class="abs copy" style="left:9px;top:52px;width:176px;font-size:7.3px;line-height:13px">
    <p>Wayfarer Assure Group, a leading provider of group travel insurance, offers participants the opportunity to protect their travel investment.</p>
    <p style="margin-top:13px">This program offers an array of <b>travel protection</b> benefits including 24/7 Worldwide Non-Insurance Assistance Services as well as Trip Cancellation, Trip Interruption, Medical Expense, Baggage and Personal Effects, and more travel insurance coverages such as the Cancel for Any Reason (CFAR) option, if eligible.</p>
  </div>
  <p class="abs prompt" style="left:9px;top:231px;width:180px;font-size:10.5px;line-height:14px">To start, please enter your total Trip Cost: $_______</p>

  <div class="plan-flag" style="left:8px;top:273px;width:179px;height:24px;font-size:7.5px;line-height:24px">RECOMMENDED</div>
  <article class="plan" style="left:8px;top:297px;width:179px;height:258px;border-top:0">
    <h3 class="plan-name" style="font-size:11.5px;line-height:15px;margin-top:18px">Scholar Prime<br>with CFAR</h3>
    <p class="plan-price" style="font-size:11px;margin-top:8px"><sup>$</sup>100</p>
    <p class="plan-lead" style="font-size:6.5px;line-height:10px;margin:11px 10px 0">Protects your trip investment if you need to cancel for any reason***</p>
    <ul class="plan-list" style="font-size:6.2px;line-height:10px;margin:8px 6px 0 8px">
      <li><svg class="icon" width="9" height="9"><use href="#tick"/></svg><span>Trip Cancellation coverage provides a 100% refund if you need to cancel for covered reasons</span></li>
      <li style="margin-top:6px"><svg class="icon" width="9" height="9"><use href="#tick"/></svg><span>Includes additional coverages as per below Schedule</span></li>
      <li style="margin-top:6px"><svg class="icon" width="9" height="9"><use href="#tick"/></svg><span>Includes Cancel for Any Reason (CFAR)***</span></li>
      <li style="margin-top:6px"><svg class="icon" width="9" height="9"><use href="#tick"/></svg><span>Covers cancellation due to fear of a pandemic ***</span></li>
    </ul>
    <a class="more-link" href="#" style="top:224px;font-size:7px">MORE INFORMATION <svg class="icon" width="14" height="9"><use href="#arrow"/></svg></a>
  </article>
  <div class="select-btn" style="left:58px;top:543px;width:85px;height:23px;font-size:8.5px;line-height:23px">SELECT</div>

  <article class="plan" style="left:10px;top:577px;width:177px;height:265px">
    <h3 class="plan-name" style="font-size:11.5px;margin-top:18px">Scholar Prime</h3>
    <p class="plan-price" style="font-size:11px;margin-top:8px"><sup>$</sup>100</p>
    <p class="plan-lead" style="font-size:6.5px;line-height:10px;margin:12px 22px 0">Protects your trip investment for covered reasons only</p>
    <ul class="plan-list" style="font-size:6.2px;line-height:10px;margin:8px 6px 0 8px">
      <li><svg class="icon" width="9" height="9"><use href="#tick"/></svg><span>Trip Cancellation coverage provides a 100% refund if you need to cancel for covered reasons</span></li>
      <li style="margin-top:7px"><svg class="icon" width="9" height="9"><use href="#tick"/></svg><span>Includes additional coverages as per below Schedule</span></li>
      <li class="no" style="margin-top:10px"><svg class="icon" width="9" height="9"><use href="#cross"/></svg><span>Does NOT include Cancel for Any Reason (CFAR)***</span></li>
      <li class="no" style="margin-top:11px"><svg class="icon" width="9" height="9"><use href="#cross"/></svg><span>No coverage for cancellations due to fear of a pandemic</span></li>
    </ul>
    <a class="more-link" href="#" style="top:226px;font-size:7px">MORE INFORMATION <svg class="icon" width="14" height="9"><use href="#arrow"/></svg></a>
  </article>
  <div class="select-btn" style="left:56px;top:830px;width:85px;height:23px;font-size:8.5px;line-height:23px">SELECT</div>

  <article class="plan" style="left:10px;top:860px;width:177px;height:155px">
    <h3 class="plan-name" style="font-size:11.5px;margin-top:14px">None</h3>
    <p class="plan-price" style="font-size:11px;margin-top:7px"><sup>$</sup>0</p>
    <p class="plan-lead" style="font-size:6.5px;line-height:10px;margin:10px 40px 0">Potentially lose 100% of your tour cost</p>
    <ul class="plan-list" style="font-size:6.5px;margin:12px 8px 0"><li class="dot">No Payment Protection</li></ul>
    <a class="more-link" href="#" style="top:121px;font-size:7px">MORE INFORMATION <svg class="icon" width="14" height="9"><use href="#arrow"/></svg></a>
  </article>
  <div class="select-btn" style="left:54px;top:1004px;width:85px;height:23px;font-size:8.5px;line-height:23px">SELECT</div>
</section>

<table class="abs benefits" style="left:1186px;top:1525px;width:196px;font-size:5.8px">
  <colgroup><col style="width:104px"><col style="width:30px"><col></colgroup>
  <thead><tr style="height:30px"><th style="font-size:11.5px;padding-left:5px;padding-top:8px;background:#fff">Benefit</th><th style="background:#fff">NONE</th><th style="background:#fff;line-height:10px">SCHOLAR<br>PRIME</th></tr></thead>
  <tbody>
  <tr style="height:30px"><td class="name" style="padding-left:5px">CANCEL FOR ANY REASON<br>(CFAR)***</td><td><svg class="icon" width="10" height="10" style="margin-left:9px"><use href="#cross"/></svg></td><td><svg class="icon" width="10" height="10" style="margin-left:20px"><use href="#cross"/></svg></td></tr>
  <tr style="height:26px"><td class="name" style="padding-left:5px">Trip Cancellation**</td><td><svg class="icon" width="10" height="10" style="margin-left:9px"><use href="#cross"/></svg></td><td style="padding-left:5px">Trip Cost*</td></tr>
  <tr style="height:26px"><td class="name" style="padding-left:5px">Trip Interruption**</td><td><svg class="icon" width="10" height="10" style="margin-left:9px"><use href="#cross"/></svg></td><td>150% Trip Cost</td></tr>
  <tr style="height:25px"><td class="name" style="padding-left:5px">Travel Delay – 6 Hours</td><td><svg class="icon" width="10" height="10" style="margin-left:9px"><use href="#cross"/></svg></td><td>$750 ($150/day)</td></tr>
  <tr style="height:33px"><td class="name" style="padding-left:5px">Missed Connection –<br>3 Hours</td><td><svg class="icon" width="10" height="10" style="margin-left:9px"><use href="#cross"/></svg></td><td>$500</td></tr>
  <tr style="height:29px"><td class="name" style="padding-left:5px">Baggage/Personal Effects</td><td><svg class="icon" width="10" height="10" style="margin-left:9px"><use href="#cross"/></svg></td><td>$1,500</td></tr>
  <tr style="height:23px"><td class="name" style="padding-left:5px">Baggage Delay – 24 Hours</td><td><svg class="icon" width="10" height="10" style="margin-left:9px"><use href="#cross"/></svg></td><td>$300</td></tr>
  <tr style="height:42px"><td class="name" style="padding-left:5px">Emergency Medical Evacuation,<br>Medical Repatriation &amp; Return<br>of Remains</td><td><svg class="icon" width="10" height="10" style="margin-left:9px"><use href="#cross"/></svg></td><td>$100,000</td></tr>
  <tr style="height:33px"><td class="name" style="padding-left:5px">Accident &amp; Sickness Medical<br>Expense</td><td><svg class="icon" width="10" height="10" style="margin-left:9px"><use href="#cross"/></svg></td><td>$25,000</td></tr>
  <tr style="height:34px"><td class="name" style="padding-left:5px">Non-Medical Emergency<br>Evacuation</td><td><svg class="icon" width="10" height="10" style="margin-left:9px"><use href="#cross"/></svg></td><td>$100,000</td></tr>
  <tr style="height:32px"><td class="name" style="padding-left:5px">Non-Insurance Worldwide<br>Emergency Assistance Services</td><td><svg class="icon" width="10" height="10" style="margin-left:9px"><use href="#cross"/></svg></td><td>Included</td></tr>
  </tbody>
</table>
<span class="abs" style="left:1186px;top:1886px;width:196px;height:2px;background:var(--rule)"></span>
<span class="abs" style="left:1235px;top:1887px;width:78px;height:4px;border-radius:2px;background:#333"></span>

<div class="abs notes" style="left:1195px;top:1905px;width:180px;font-size:6.4px;line-height:10.4px">
  <p>Coverages may vary and not all coverage is available in all jurisdictions. Totals listed below each coverage are the maximum benefit amount payable.</p>
  <p style="margin-top:10px">* Up to the lesser of the Trip Cost paid or the limit of Coverage for which benefits are requested and the appropriate plan cost has been paid. Maximum limit of $10,000</p>
  <p style="margin-top:10px">** For $0 Trip Cost, there is no Trip Cancellation and Trip Interruption is limited to $500 return air only</p>
  <p style="margin-top:10px">*** CFAR coverage is the lessor of 75% of the nonrefundable trip cost or up to the maximum of $10,000. CFAR is optional and available for purchase on an individual level. Trip cancellation must be 48 hours or more prior to scheduled departure. CFAR must be purchased at the time of plan purchase and with, or before your final payment. CFAR is available if you paid your Travel Supplier for the full cost for all non-refundable trip costs for your trip prior to your cancellation of your trip. For $0 Trip Cost there is no CFAR. <b>This benefit is not available to residents of New York State.</b></p>
</div>
<a class="abs limits-btn" href="#" style="left:1208px;top:2172px;width:153px;height:16px;font-size:6px;line-height:16px;text-decoration:none">Click here for limitations and exclusions</a>

<footer class="abs site-footer" style="left:1186px;top:2200px;width:196px;height:38px;font-size:4.2px;text-align:center">
  <p style="padding:5px 6px 0;line-height:6.5px">© 2020 HALVARD TOURS, INC. &nbsp; CONTACT US &nbsp; (800) 555-0142 &nbsp; PRIVACY POLICY &nbsp; RESPONSIBILITY</p>
  <span class="abs secure-badge" style="left:5px;top:19px;width:56px;height:14px"><i style="width:9px"></i></span>
</footer>

</main>
</body>
</html>
```